BRAMBLE CABS

Taxi card design

Need changes very slow in replying to my messages.

Target Market(s)

Customers

Industry/Entity Type

Taxi

Contact Information for Business Card

See previous design

Font styles to use
Sans Serif

Colors
A7469A
B969AE
D3A5CF
EDDBEB
F8F0F9
6B429C
8869AF
B7A5CE
E3DAEB
F3F0F8

Requirements
Nice to have
• We are in the business of looking after people, not just driving vehicles front
Should not have
• Front number 01832 419 526 needs to big big

```html
<!DOCTYPE html>
<html lang="en">
<head>
<meta charset="utf-8">
<title>Bramble Cabs – Business Card</title>
<link href="https://fonts.googleapis.com/css2?family=Montserrat:wght@500;600;700;800&display=swap" rel="stylesheet">
<style>
  :root{
    --magenta:#A7469A;
    --magenta-light:#B969AE;
    --purple:#6B429C;
    --purple-deep:#4f2f80;
    --ink:#151515;
    --paper:#ffffff;
    --canvas:#f1f1f1;
  }
  *{box-sizing:border-box;margin:0;padding:0}
  html,body{width:1109px;height:1200px;overflow:hidden}
  body{background:var(--canvas);font-family:'Montserrat',sans-serif;position:relative}
  .card{position:absolute;top:465px;width:480px;height:270px;border-radius:30px;overflow:hidden;box-shadow:0 6px 14px rgba(0,0,0,.22)}
  .card-front{left:44px;background:linear-gradient(100deg,var(--magenta) 0%,#8a4aa0 55%,var(--purple) 100%)}
  .card-back{left:585px;background:var(--paper)}

  /* front */
  .front-texture{position:absolute;inset:0;background:linear-gradient(180deg,rgba(255,255,255,.07),rgba(255,255,255,0) 60%)}
  .front-brand{position:absolute;left:0;right:0;top:96px;text-align:center;color:#fff;font-weight:800;font-size:44px;letter-spacing:1px}
  .front-phone{position:absolute;left:0;right:0;top:168px;display:flex;justify-content:center;align-items:center;gap:12px;color:#fff;font-weight:800;font-size:24px;letter-spacing:3px}
  .phone-badge{width:28px;height:28px;border-radius:7px;background:#fff;display:flex;align-items:center;justify-content:center}

  /* back */
  .back-shape{position:absolute;inset:0}
  .back-brand{position:absolute;left:18px;top:32px;display:flex;align-items:flex-end;gap:8px}
  .brand-name{color:var(--purple);font-weight:800;font-size:24px;line-height:1}
  .brand-service{color:var(--ink);font-weight:800;font-size:16px;line-height:1}
  .brand-service small{display:block;font-size:8px;color:var(--magenta);letter-spacing:.5px}
  .brand-est{position:absolute;left:18px;top:62px;font-size:7px;font-weight:600;letter-spacing:1.6px;color:var(--ink)}
  .contact-list{position:absolute;left:0;top:86px;list-style:none}
  .contact-item{display:flex;align-items:flex-start;height:25px;font-size:11.5px;font-weight:500;color:var(--ink)}
  .contact-tab{width:26px;height:16px;background:var(--ink);margin-right:-6px}
  .contact-icon{width:17px;height:17px;border-radius:50%;background:#fff;border:1.6px solid var(--magenta);display:flex;align-items:center;justify-content:center;margin-top:-0.5px;margin-right:10px}
  .contact-item address{font-style:normal;line-height:1.3}
  .services{position:absolute;right:16px;top:44px;text-align:right;color:#fff;font-weight:700;font-size:15px;letter-spacing:1px;line-height:17px}
  .service{margin-bottom:12px}
  .service-phones{position:absolute;right:16px;top:172px;list-style:none;color:#fff;font-weight:600;font-size:12.5px;letter-spacing:2px;line-height:16.5px}
  .service-phones li{display:flex;align-items:center;gap:4px;justify-content:flex-end}
</style>
</head>
<body>

<section class="card card-front">
  <div class="front-texture" role="img" aria-label="Soft repeating brand name pattern"></div>
  <div class="front-brand">BRAMBLE CABS</div>
  <div class="front-phone">
    <span class="phone-badge"><svg width="16" height="16" viewBox="0 0 24 24"><path d="M6.6 10.8a15.1 15.1 0 0 0 6.6 6.6l2.2-2.2a1 1 0 0 1 1-.25 11.4 11.4 0 0 0 3.6.57 1 1 0 0 1 1 1V20a1 1 0 0 1-1 1A17 17 0 0 1 3 4a1 1 0 0 1 1-1h3.5a1 1 0 0 1 1 1c0 1.25.2 2.45.57 3.57a1 1 0 0 1-.25 1z" fill="none" stroke="#A7469A" stroke-width="2.2"/></svg></span>
    <span>01832 419 526</span>
  </div>
</section>

<section class="card card-back">
  <svg class="back-shape" width="480" height="270" viewBox="0 0 480 270">
    <defs>
      <linearGradient id="panelGrad" x1="0" y1="1" x2="1" y2="0">
        <stop offset="0" stop-color="#A7469A"/>
        <stop offset="1" stop-color="#4f2f80"/>
      </linearGradient>
    </defs>
    <path d="M372 0H480V270H165L268 170L256 150L262 96Z" fill="url(#panelGrad)"/>
    <path d="M270 86H480V90H266Z M258 112H480V116H258Z M258 158H480V162H258Z" fill="#3d2266" opacity=".55"/>
  </svg>

  <div class="back-brand">
    <span class="brand-name">BRAMBLE CABS</span>
    <span class="brand-service">24/7<small>SERVICE</small></span>
  </div>
  <div class="brand-est">ESTABLISHED SINCE 1986</div>

  <ul class="contact-list">
    <li class="contact-item"><span class="contact-tab"></span><span class="contact-icon"><svg width="9" height="9" viewBox="0 0 24 24"><path d="M6.6 10.8a15 15 0 0 0 6.6 6.6l2.2-2.2 5.6 1.8V21A18 18 0 0 1 3 3h4l1.8 5.6z" fill="#A7469A"/></svg></span>0800 555 0 147</li>
    <li class="contact-item"><span class="contact-tab"></span><span class="contact-icon"><svg width="9" height="9" viewBox="0 0 24 24"><rect x="2" y="5" width="20" height="14" rx="2" fill="none" stroke="#A7469A" stroke-width="2.5"/><path d="M2 6l10 7 10-7" fill="none" stroke="#A7469A" stroke-width="2.5"/></svg></span>bramblecabs@mailbox.co.uk</li>
    <li class="contact-item"><span class="contact-tab"></span><span class="contact-icon"><svg width="9" height="9" viewBox="0 0 24 24"><circle cx="12" cy="12" r="9" fill="none" stroke="#A7469A" stroke-width="2.5"/><path d="M3 12h18M12 3c4 4 4 14 0 18M12 3c-4 4-4 14 0 18" fill="none" stroke="#A7469A" stroke-width="2"/></svg></span>www.bramblecabs.co.uk</li>
    <li class="contact-item"><span class="contact-tab"></span><span class="contact-icon"><svg width="9" height="9" viewBox="0 0 24 24"><path d="M12 22s7-7 7-12a7 7 0 0 0-14 0c0 5 7 12 7 12z" fill="none" stroke="#A7469A" stroke-width="2.5"/><circle cx="12" cy="10" r="2.5" fill="#A7469A"/></svg></span>
      <address>Orchard Lane Hall<br>Mill Row<br>Hollowmere<br>HM4 7QT</address></li>
  </ul>

  <div class="services">
    <div class="service">AIRPORT<br>TRANSFERS</div>
    <div class="service">MINIBUSES</div>
    <div class="service">SCHOOL<br>TRANSPORT</div>
  </div>
  <ul class="service-phones">
    <li><svg width="11" height="11" viewBox="0 0 24 24"><path d="M6.6 10.8a15 15 0 0 0 6.6 6.6l2.2-2.2 5.6 1.8V21A18 18 0 0 1 3 3h4l1.8 5.6z" fill="none" stroke="#fff" stroke-width="2.4"/></svg>01832 41 22 22</li>
    <li><svg width="11" height="11" viewBox="0 0 24 24"><path d="M6.6 10.8a15 15 0 0 0 6.6 6.6l2.2-2.2 5.6 1.8V21A18 18 0 0 1 3 3h4l1.8 5.6z" fill="none" stroke="#fff" stroke-width="2.4"/></svg>01832 30 30 30</li>
    <li><svg width="11" height="11" viewBox="0 0 24 24"><path d="M6.6 10.8a15 15 0 0 0 6.6 6.6l2.2-2.2 5.6 1.8V21A18 18 0 0 1 3 3h4l1.8 5.6z" fill="none" stroke="#fff" stroke-width="2.4"/></svg>01832 41 77 55</li>
  </ul>
</section>

</body>
</html>
```